Load Up Your Cart

Require two banners with a size of 980 x 450 pixels
Similar natural looking banner as per attachment. The background is supposed to be a cardboard carton
price "$9.95"
Wording and layout the same as attached file

```html
<!DOCTYPE html>
<html lang="en">
<head>
<meta charset="utf-8">
<title>Load Up Your Cart – Flat Rate Shipping Banner</title>
<link rel="stylesheet" href="https://fonts.googleapis.com/css2?family=Arimo:wght@700&family=Archivo+Narrow:wght@700&display=swap">
<style>
  :root {
    --page-bg: #000000;
    --carton-light: #b48c5c;
    --carton-mid: #a67c4d;
    --carton-dark: #8a6337;
    --fold-shadow: #5e3d1c;
    --stamp-ink: #6b3b12;
    --print-ink: #3b2410;
    --headline: #ffffff;
    --headline-edge: #8e7a66;
  }
  * { margin: 0; padding: 0; box-sizing: border-box; }
  html, body {
    width: 1200px; height: 1000px; overflow: hidden;
    background: var(--page-bg);
  }
  .canvas { position: relative; width: 1200px; height: 1000px; }

  .shipping-banner {
    position: absolute; left: 232px; top: 331px;
    width: 736px; height: 338px; overflow: hidden;
  }
  .carton-surface {
    position: absolute; inset: 0;
    background:
      radial-gradient(ellipse at 35% 40%, var(--carton-light) 0%, var(--carton-mid) 60%, var(--carton-dark) 100%);
  }
  .banner-art { position: absolute; inset: 0; }

  .price {
    position: absolute; left: 0; width: 100%; padding-left: 240px; top: 20px;
    text-align: center;
    font-family: "Arimo", Arial, sans-serif; font-weight: 700;
    font-size: 115px; line-height: 1; letter-spacing: 2px;
    color: var(--headline);
    text-shadow: 0 0 2px var(--headline-edge), 2px 3px 3px rgba(60,35,15,.55);
  }
  .offer {
    position: absolute; left: 276px; top: 141px;
    font-family: "Arimo", Arial, sans-serif; font-weight: 700;
    font-size: 48px; line-height: 1;
    color: var(--headline);
    text-shadow: 0 0 2px var(--headline-edge), 2px 2px 3px rgba(60,35,15,.55);
  }
  .tagline {
    position: absolute; left: 251px; top: 211px;
    font-family: "Archivo Narrow", "Arial Narrow", sans-serif; font-weight: 700;
    font-size: 28.5px; line-height: 1; letter-spacing: .2px; white-space: nowrap;
    color: var(--headline);
    text-shadow: 0 0 2px var(--headline-edge), 1px 2px 2px rgba(60,35,15,.55);
  }
  .handling-icons {
    position: absolute; left: 518px; top: 265px;
    display: flex; gap: 6px;
  }
  .handling-icon { width: 64px; height: 62px; }
</style>
</head>
<body>
<main class="canvas">
  <section class="shipping-banner">
    <div class="carton-surface" role="img" aria-label="Brown corrugated cardboard carton texture"></div>

    <svg class="banner-art" viewBox="0 0 736 338" width="736" height="338">
      <polygon class="fold-top" points="660,0 736,0 736,78" fill="var(--fold-shadow)" opacity=".75"/>
      <polygon class="fold-bottom" points="0,200 140,338 0,338" fill="var(--fold-shadow)" opacity=".55"/>

      <g class="stamp" transform="rotate(-15 145 131)" fill="var(--stamp-ink)" font-family="Arimo, Arial, sans-serif" font-weight="700">
        <circle cx="145" cy="131" r="116" fill="none" stroke="var(--stamp-ink)" stroke-width="7"/>
        <text x="140" y="118" text-anchor="middle" font-size="56">LOAD</text>
        <text x="108" y="190" text-anchor="middle" font-size="64">UP</text>
        <text x="205" y="152" text-anchor="middle" font-size="24">YOUR</text>
        <text x="207" y="178" text-anchor="middle" font-size="24">CART</text>
      </g>
    </svg>

    <h1 class="price">$9.95</h1>
    <p class="offer">Flat Rate Shipping</p>
    <p class="tagline">NO MINIMUNS. NO CODES. NO GIMMICKS</p>

    <div class="handling-icons">
      <svg class="handling-icon" viewBox="0 0 64 62" aria-label="This way up">
        <rect x="2" y="2" width="60" height="58" rx="4" fill="none" stroke="var(--print-ink)" stroke-width="2.5"/>
        <path d="M22 44V18M14 26l8-10 8 10M42 44V18M34 26l8-10 8 10" fill="none" stroke="var(--print-ink)" stroke-width="5"/>
        <rect x="12" y="48" width="40" height="5" fill="var(--print-ink)"/>
      </svg>
      <svg class="handling-icon" viewBox="0 0 64 62" aria-label="Keep dry">
        <rect x="2" y="2" width="60" height="58" rx="4" fill="none" stroke="var(--print-ink)" stroke-width="2.5"/>
        <g fill="var(--print-ink)">
          <circle cx="18" cy="10" r="1.5"/><circle cx="28" cy="8" r="1.5"/><circle cx="38" cy="10" r="1.5"/><circle cx="47" cy="8" r="1.5"/>
          <path d="M8 30 Q32 8 56 30 Q50 26 44 30 Q38 26 32 30 Q26 26 20 30 Q14 26 8 30Z"/>
        </g>
        <path d="M32 30v18a4 4 0 0 1-8 0" fill="none" stroke="var(--print-ink)" stroke-width="3"/>
      </svg>
      <svg class="handling-icon" viewBox="0 0 64 62" aria-label="Fragile">
        <rect x="2" y="2" width="60" height="58" rx="4" fill="none" stroke="var(--print-ink)" stroke-width="2.5"/>
        <path d="M20 10h24l-2 14a10 10 0 0 1-20 0Z" fill="var(--print-ink)"/>
        <path d="M34 10l-4 7 5 3-4 6" fill="none" stroke="var(--carton-mid)" stroke-width="2"/>
        <path d="M32 34v16M24 52h16" stroke="var(--print-ink)" stroke-width="4"/>
      </svg>
    </div>
  </section>
</main>
</body>
</html>
```